Wendlake Business Cards

Front and back. Martin Colfax MBA is the CEO of Wendlake Homes. Black white and grays. Logo and cool design.

Target Market(s)

Professional lenders and investors

Industry/Entity Type

Real estate developer. NO HOUSES OR ROOFS

Contact Information for Business Card

Logo, name and unique design. Front and back. Martin Colfax MBA is the CEO of Wendlake Homes. Black white and grays. Logo and cool design.

Font styles to use
Sans Serif

Colors

Designer to choose only greyscale colors for use in the design.

Requirements
Must have
• Cool look. Not the same card I could design.
Nice to have
• Something memorable
Should not have
• Basic

```html
<!DOCTYPE html>
<html lang="en">
<head>
<meta charset="utf-8">
<title>Wendlake Homes – Business Cards</title>
<link href="https://fonts.googleapis.com/css2?family=Poppins:wght@300;400;600;700&display=swap" rel="stylesheet">
<style>
  :root {
    --stage: #262626;
    --card: #0b0b0b;
    --card-sheen: #171717;
    --card-edge: #1c1c1c;
    --ink: #ffffff;
    --ink-soft: #bdbdbd;
    --ink-muted: #9a9a9a;
    --rule: #555555;
    --silver: #d9d9d9;
  }
  * { box-sizing: border-box; margin: 0; padding: 0; }
  html, body { width: 1200px; height: 900px; overflow: hidden; }
  body {
    background: var(--stage);
    font-family: "Poppins", sans-serif;
    display: flex;
    align-items: center;
    justify-content: center;
    gap: 40px;
  }
  .card {
    width: 540px;
    height: 308px;
    background: linear-gradient(135deg, var(--card-sheen) 0%, var(--card) 55%);
    border: 1px solid var(--card-edge);
    border-radius: 20px;
    position: relative;
    color: var(--ink);
  }

  /* Contact side */
  .card--contact {
    display: flex;
    align-items: center;
    padding: 0 30px 0 38px;
  }
  .card--contact .brand-name {
    width: 200px;
    margin-top: 96px;
    font-size: 30px;
    font-weight: 700;
    line-height: 1.05;
    letter-spacing: -0.6px;
    color: var(--ink);
  }
  .divider {
    flex: none;
    width: 1px;
    height: 176px;
    background: var(--rule);
    margin: 0 22px 0 12px;
  }
  .details { flex: 1; min-width: 0; }
  .person-name {
    font-size: 20px;
    font-weight: 600;
    line-height: 1.15;
    white-space: nowrap;
  }
  .person-title {
    font-size: 13px;
    font-weight: 300;
    color: var(--ink-muted);
    margin-bottom: 12px;
  }
  .contact-list { list-style: none; }
  .contact-list li {
    display: flex;
    align-items: center;
    gap: 8px;
    font-size: 13px;
    font-weight: 300;
    line-height: 1.65;
    color: var(--ink-soft);
    white-space: nowrap;
  }
  .contact-list svg { width: 13px; height: 13px; flex: none; }
  .address {
    margin-top: 10px;
    padding-left: 21px;
    font-size: 13px;
    font-weight: 300;
    font-style: normal;
    line-height: 1.4;
    color: var(--ink-soft);
    white-space: nowrap;
  }

  /* Brand side */
  .card--brand {
    display: flex;
    align-items: center;
    justify-content: center;
  }
  .card--brand .brand-name {
    font-size: 46px;
    font-weight: 700;
    letter-spacing: -1px;
    color: var(--silver);
  }
</style>
</head>
<body>
  <section class="card card--contact" aria-label="Business card, contact side">
    <div class="brand-name">Wendlake<br>Homes</div>
    <div class="divider"></div>
    <div class="details">
      <h1 class="person-name">Martin Colfax MBA</h1>
      <p class="person-title">Chief Executive Officer</p>
      <ul class="contact-list">
        <li>
          <svg viewBox="0 0 16 16" aria-hidden="true"><path d="M3.5 1.5h2.5l1.2 3-1.6 1.2a9 9 0 004.7 4.7l1.2-1.6 3 1.2v2.5c0 .8-.7 1.5-1.5 1.5A12.5 12.5 0 012 3c0-.8.7-1.5 1.5-1.5z" fill="none" stroke="#ffffff" stroke-width="1.4"/></svg>
          044-555 018 274
        </li>
        <li>
          <svg viewBox="0 0 16 16" aria-hidden="true"><rect x="1" y="3" width="14" height="10" fill="#ffffff"/><path d="M1 3l7 6 7-6" fill="none" stroke="#0b0b0b" stroke-width="1.2"/></svg>
          info@wendlakehomes.com
        </li>
        <li>
          <svg viewBox="0 0 16 16" aria-hidden="true"><g fill="none" stroke="#ffffff" stroke-width="1.2"><circle cx="8" cy="8" r="6.5"/><ellipse cx="8" cy="8" rx="3" ry="6.5"/><path d="M1.5 8h13M2.5 4.8h11M2.5 11.2h11"/></g></svg>
          www.wendlakehomes.com
        </li>
      </ul>
      <address class="address">18 Harrow Quay, Suite 400<br>45120, Northbridge</address>
    </div>
  </section>

  <section class="card card--brand" aria-label="Business card, brand side">
    <div class="brand-name">Wendlake Homes</div>
  </section>
</body>
</html>
```